Business Card Design Project

I am community manager and social media strategist. I need a double sided business card with company logo and name. Looking for something professional, elegant but also a little bit original.

Industry/Entity Type

Business

Requirements
Must have
• - The logo and the colours are the company colours and a required to stay.
- The size should be: 84 x 55 mm (or 3.30 x 2.16)
- The file size should be: 1039 x 697 pixels (300 dpi)
- I'd like rounded corners. :)

Use the following contact information for the card:

Lucile Bravant
Stratégie médias sociaux / community management / édition de sites sociaux
mob. : 0687152930
lucile.bravant@maivox.fr
Chirp. : @lbravant
Vocall : bravant.lucile

```html
<!DOCTYPE html>
<html lang="fr">
<head>
<meta charset="utf-8">
<title>Avelia – business card, front and back</title>
<link rel="stylesheet" href="https://fonts.googleapis.com/css2?family=Cutive+Mono&family=Open+Sans:wght@400;700&display=swap">
<style>
  :root {
    --stage: #101310;
    --card-front: #f1f2f4;
    --card-back: #135a8c;
    --card-edge: #1a1a1a;
    --brand-blue: #1f6fa8;
    --deco-front: rgba(150, 170, 200, 0.35);
    --deco-back: rgba(255, 255, 255, 0.18);
    --ink-grey: #5a5a5a;
    --ink-name: #555555;
    --white: #ffffff;
  }
  * { margin: 0; padding: 0; box-sizing: border-box; }
  html, body { width: 1200px; height: 846px; overflow: hidden; }
  body { background: var(--stage); position: relative; font-family: "Open Sans", Arial, sans-serif; }

  .card {
    position: absolute;
    width: 462px;
    height: 294px;
    border-radius: 18px;
    border: 2px solid var(--card-edge);
    overflow: hidden;
  }
  .card--front { left: 178px; top: 84px; background: var(--card-front); }
  .card--back { left: 450px; top: 469px; background: var(--card-back); }

  .card__deco { position: absolute; left: -150px; top: -20px; width: 330px; height: 330px; border-radius: 50%; }
  .card--front .card__deco { background: var(--deco-front); }
  .card--back .card__deco { background: var(--deco-back); }

  .brand { position: absolute; display: flex; flex-direction: column; align-items: center; }
  .brand__dot { border-radius: 50%; }
  .brand__name { font-weight: 700; letter-spacing: 1px; line-height: 1; }

  .card--front .brand { right: 14px; top: 12px; width: 160px; }
  .card--front .brand__dot { width: 88px; height: 88px; background: var(--brand-blue); margin-bottom: 12px; }
  .card--front .brand__name { font-size: 34px; color: var(--brand-blue); }

  .card--back .brand { right: 22px; top: 14px; width: 210px; }
  .card--back .brand__dot { width: 104px; height: 104px; background: var(--white); margin-bottom: 22px; }
  .card--back .brand__name { font-size: 44px; color: var(--white); }

  .holder { position: absolute; left: 258px; top: 174px; }
  .holder__name { font-family: "Cutive Mono", "Courier New", monospace; font-size: 27px; color: var(--ink-name); line-height: 1; margin-bottom: 14px; }
  .holder__role { font-size: 12px; line-height: 16px; color: var(--ink-grey); }

  .contact { position: absolute; left: 131px; top: 252px; color: var(--white); font-size: 13.5px; line-height: 18px; }
</style>
</head>
<body>
  <section class="card card--front" aria-label="Card front">
    <div class="card__deco"></div>
    <div class="brand">
      <span class="brand__dot"></span>
      <span class="brand__name">AVELIA</span>
    </div>
    <div class="holder">
      <p class="holder__name">Lucile Bravant</p>
      <p class="holder__role">Stratégie médias sociaux /<br>community management /<br>édition de sites sociaux</p>
    </div>
  </section>

  <section class="card card--back" aria-label="Card back">
    <div class="card__deco"></div>
    <div class="brand">
      <span class="brand__dot"></span>
      <span class="brand__name">AVELIA</span>
    </div>
    <div class="contact">
      <p>mob. : 0687152930 | lucile.bravant@maivox.fr</p>
      <p>Chirp. : @lbravant | Vocall : bravant.lucile</p>
    </div>
  </section>
</body>
</html>
```